Funeral Insurance Infographic

I need some information about infographic turned into an infographic.

Details are as follows:

Entry Ages: 45 - 70
Expiry age: No expiry age
Minimum Sum Insured: $5,000
Maximum Sum Insured: $10,000
Cooling off period: 30 Days

First two years of policy benefit if not paid if death is caused by suicide

Accidental only covered in first 2 years - no other deaths covered.

All deaths covered after that

Available for Australian residents only

```html
<!DOCTYPE html>
<html lang="en">
<head>
<meta charset="utf-8">
<title>Funeral Insurance Infographic</title>
<link rel="stylesheet" href="https://fonts.googleapis.com/css2?family=Great+Vibes&family=Roboto+Condensed:wght@700;900&display=swap">
<style>
  :root {
    --page-top: #f4f4f2;
    --page-side: #d9d9d6;
    --rule: #111111;
    --ribbon: #7a5331;
    --ribbon-dark: #5a3a20;
    --ribbon-tail: #b08a5c;
    --cream: #fbf3e4;
    --tile-tan: #c49a6c;
    --tile-sage: #b8b397;
    --ink: #111111;
    --red: #e0201c;
    --white: #ffffff;
    --band: #7a5331;
    --note-orange: #f7a21b;
    --flag-blue: #1c2f7a;
  }
  * { box-sizing: border-box; margin: 0; padding: 0; }
  html, body { width: 974px; height: 1200px; overflow: hidden; }
  body {
    position: relative;
    background: linear-gradient(90deg, var(--page-side) 0%, var(--page-top) 8%, var(--page-top) 92%, var(--page-side) 100%);
    font-family: "Roboto Condensed", "Arial Narrow", sans-serif;
    color: var(--ink);
  }
  .rule { position: absolute; left: 0; width: 974px; height: 8px; background: var(--rule); }
  .rule--top { top: 22px; }
  .rule--bottom { top: 1168px; }

  .banner { position: absolute; left: 0; top: 50px; width: 974px; height: 240px; }
  .banner__title {
    position: absolute; left: 152px; top: 28px; width: 648px;
    text-align: center; font-family: "Great Vibes", cursive;
    color: var(--cream); font-size: 74px; line-height: 76px;
    text-shadow: 2px 2px 0 var(--ribbon-dark);
  }

  .tile {
    position: absolute; width: 244px; height: 244px; border-radius: 16px;
    box-shadow: 8px 10px 12px rgba(0,0,0,0.45);
    overflow: hidden;
  }
  .tile--tan { background: var(--tile-tan); }
  .tile--sage { background: var(--tile-sage); }
  .tile--ages { left: 61px; top: 327px; }
  .tile--expiry { left: 353px; top: 327px; }
  .tile--sum { left: 645px; top: 327px; }
  .tile--cooling { left: 61px; top: 621px; }
  .tile--suicide { left: 353px; top: 621px; }
  .tile--accident { left: 645px; top: 621px; }

  .art { position: absolute; border-radius: 6px; }

  .ages__art { left: 22px; top: 16px; width: 200px; height: 130px; background: linear-gradient(180deg, #2a2a2a, #111); opacity: .85; }
  .ages__label { position: absolute; left: 0; top: 152px; width: 244px; text-align: center; font-weight: 900; font-size: 34px; line-height: 38px; }

  .expiry__sign { position: absolute; left: 10px; top: 4px; width: 224px; height: 224px; }
  .expiry__note { position: absolute; left: 0; top: 220px; width: 244px; text-align: center; font-size: 12px; color: var(--white); font-weight: 700; }

  .sum__max, .sum__min { position: absolute; left: 12px; font-weight: 900; font-size: 34px; line-height: 38px; color: var(--red); }
  .sum__max { top: 10px; }
  .sum__min { top: 196px; }
  .sum__bracket { position: absolute; left: 110px; top: 16px; width: 24px; height: 212px; }
  .sum__label { position: absolute; left: 22px; top: 96px; width: 84px; font-weight: 700; font-size: 22px; line-height: 26px; text-align: center; }
  .sum__tag { position: absolute; background: var(--red); color: var(--white); font-size: 13px; font-weight: 700; padding: 3px 8px; border-radius: 3px; }
  .sum__tag--max { left: 168px; top: 18px; }
  .sum__tag--min { left: 172px; top: 200px; }
  .sum__art { left: 146px; top: 52px; width: 86px; height: 136px; background: linear-gradient(160deg, #8fcf7a, #3f9a48); }

  .cooling__art { left: 8px; top: 30px; width: 66px; height: 190px; background: linear-gradient(180deg, #3b2a1e, #8a5a32 50%, #3b2a1e); }
  .cooling__note {
    position: absolute; left: 70px; top: 28px; width: 158px; height: 192px;
    background: var(--note-orange); text-align: center; padding-top: 6px;
    clip-path: polygon(0 0, 100% 0, 100% 82%, 84% 100%, 0 100%);
  }
  .cooling__head { font-weight: 900; font-size: 24px; line-height: 26px; color: var(--red); }
  .cooling__days { font-weight: 900; font-size: 80px; line-height: 84px; color: var(--red); }
  .cooling__unit { font-weight: 900; font-size: 34px; line-height: 36px; }

  .suicide__art { left: 16px; top: 18px; width: 86px; height: 166px; background: linear-gradient(180deg, #222 0 10%, #d6332a 10% 100%); opacity: .9; }
  .suicide__sign { position: absolute; left: 108px; top: 70px; font-weight: 900; font-size: 36px; line-height: 60px; white-space: nowrap; }
  .suicide__sign span { color: var(--red); font-size: 58px; }
  .suicide__text { position: absolute; left: 8px; top: 196px; width: 228px; text-align: center; font-weight: 700; font-size: 13px; line-height: 16px; }

  .accident__art { left: 10px; top: 28px; width: 224px; height: 130px; background: linear-gradient(90deg, #111 0 78%, #d6332a 78% 100%); }
  .accident__text { position: absolute; left: 8px; top: 170px; width: 228px; text-align: center; font-weight: 700; font-size: 14px; line-height: 18px; }

  .band {
    position: absolute; left: 61px; top: 921px; width: 875px; height: 228px;
    background: var(--band); border-radius: 16px;
    box-shadow: 8px 10px 12px rgba(0,0,0,0.45);
  }
  .band__art--stone { left: 22px; top: 32px; width: 150px; height: 166px; background: linear-gradient(180deg, #1a1a1a, #000); border-radius: 60px 60px 4px 4px; }
  .band__text { position: absolute; left: 180px; top: 74px; width: 480px; text-align: center; color: var(--white); font-weight: 700; }
  .band__lead { font-size: 28px; line-height: 34px; }
  .band__sub { font-size: 22px; line-height: 28px; }
  .band__art--flag { left: 646px; top: 66px; width: 164px; height: 86px; background: linear-gradient(135deg, #c8102e 0 18%, var(--flag-blue) 18% 100%); border-radius: 0; }
</style>
</head>
<body>
  <div class="rule rule--top"></div>

  <header class="banner">
    <svg width="974" height="240" viewBox="0 0 974 240" aria-hidden="true">
      <polygon points="0,40 200,40 200,200 0,200 60,120" fill="var(--ribbon-tail)"/>
      <polygon points="974,40 774,40 774,200 974,200 914,120" fill="var(--ribbon-tail)"/>
      <polygon points="152,200 200,200 200,232" fill="var(--ribbon-dark)"/>
      <polygon points="800,200 774,200 774,232" fill="var(--ribbon-dark)"/>
      <rect x="152" y="3" width="648" height="197" fill="var(--ribbon)"/>
    </svg>
    <h1 class="banner__title">Funeral Insurance<br>Infographic</h1>
  </header>

  <section class="tile tile--tan tile--ages">
    <div class="art ages__art" role="img" aria-label="Three figures of increasing age, from adult to elderly with a cane"></div>
    <p class="ages__label">45-70 y/o<br>Entry Ages</p>
  </section>

  <section class="tile tile--sage tile--expiry">
    <svg class="expiry__sign" viewBox="0 0 224 224" aria-hidden="true">
      <text x="112" y="104" text-anchor="middle" font-family="Roboto Condensed, sans-serif" font-weight="900" font-size="50" fill="var(--red)">Expiry</text>
      <text x="112" y="160" text-anchor="middle" font-family="Roboto Condensed, sans-serif" font-weight="900" font-size="50" fill="var(--red)">Age</text>
      <circle cx="112" cy="112" r="96" fill="none" stroke="var(--ink)" stroke-width="16"/>
      <line x1="44" y1="44" x2="180" y2="180" stroke="var(--ink)" stroke-width="16"/>
    </svg>
    <p class="expiry__note">No Expiry Age</p>
  </section>

  <section class="tile tile--tan tile--sum">
    <span class="sum__max">MAX</span>
    <svg class="sum__bracket" viewBox="0 0 24 212" aria-hidden="true">
      <rect x="0" y="0" width="24" height="6" fill="var(--ink)"/>
      <rect x="9" y="0" width="6" height="212" fill="var(--ink)"/>
      <rect x="0" y="206" width="24" height="6" fill="var(--ink)"/>
    </svg>
    <span class="sum__label">Sum<br>Insured</span>
    <span class="sum__tag sum__tag--max">$10000</span>
    <div class="art sum__art" role="img" aria-label="Fan of banknotes"></div>
    <span class="sum__tag sum__tag--min">$5000</span>
    <span class="sum__min">MIN</span>
  </section>

  <section class="tile tile--sage tile--cooling">
    <div class="art cooling__art" role="img" aria-label="Hourglass with falling sand"></div>
    <div class="cooling__note">
      <p class="cooling__head">Cooling Off<br>Period</p>
      <p class="cooling__days">30</p>
      <p class="cooling__unit">DAYS</p>
    </div>
  </section>

  <section class="tile tile--tan tile--suicide">
    <div class="art suicide__art" role="img" aria-label="Gallows figure symbolising suicide"></div>
    <p class="suicide__sign">= NO <span>$</span></p>
    <p class="suicide__text">First two years of policy benefit is not paid if death is caused by suicide</p>
  </section>

  <section class="tile tile--sage tile--accident">
    <div class="art accident__art" role="img" aria-label="Car striking a pedestrian, symbolising an accident"></div>
    <p class="accident__text">Accidental only covered in first 2 years - no other deaths covered.</p>
  </section>

  <section class="band">
    <div class="art band__art--stone" role="img" aria-label="Headstone with a cross"></div>
    <div class="band__text">
      <p class="band__lead">All deaths covered after that</p>
      <p class="band__sub">Available for Australian residents only</p>
    </div>
    <div class="art band__art--flag" role="img" aria-label="Australian flag"></div>
  </section>

  <div class="rule rule--bottom"></div>
</body>
</html>
```